Business Card design for new private practice opening

I need a business card design for my new private practice with my new logo uploaded as a file
On the front the logo
On the back: maybe a small logo somewhere?
Priv. Doz. DDr. Corinna Vestaluk
Fachärztin für Allgemein- & Viszeralchirurgie
Address: xxx
Tel: xxx
Mobil:xxx
Webseite:xxx
Email:xxx

Contact Information for Business Card

See project description above for details

Requirements
Nice to have
• I would like the colors of the logo incorporated into the business card

```html
<!DOCTYPE html>
<html lang="de">
<head>
<meta charset="utf-8">
<title>Vestaluk Chirurgie – Visitenkarte</title>
<link rel="stylesheet" href="https://fonts.googleapis.com/css2?family=Montserrat:wght@600&family=Arimo:wght@400;700&display=swap">
<style>
  :root {
    --stage: #2e2e2e;
    --teal: #47b9b6;
    --white: #ffffff;
    --slate: #7f7f7f;
    --slate-dark: #6f6f6f;
    --ink: #2a2a2a;
  }
  * { box-sizing: border-box; margin: 0; padding: 0; }
  html, body { width: 1200px; height: 689px; overflow: hidden; }
  body { background: var(--stage); position: relative; font-family: "Arimo", Arial, sans-serif; }

  .card {
    position: absolute;
    width: 540px;
    height: 338px;
    border-radius: 22px;
    overflow: hidden;
    top: 176px;
  }

  /* Front */
  .card--front { left: 36px; background: var(--teal); }
  .brand {
    position: absolute;
    display: flex;
    align-items: center;
    gap: 22px;
  }
  .brand__mark {
    border-radius: 50%;
    flex: none;
  }
  .brand__name {
    font-family: "Montserrat", Arial, sans-serif;
    font-weight: 600;
    line-height: 1.02;
    letter-spacing: 0.02em;
    text-transform: uppercase;
  }
  .card--front .brand { left: 62px; top: 96px; }
  .card--front .brand__mark { width: 120px; height: 120px; border: 5px solid var(--white); }
  .card--front .brand__name { color: var(--white); font-size: 44px; }

  /* Back */
  .card--back { left: 624px; background: var(--white); }
  .card__wave { position: absolute; inset: 0; width: 540px; height: 338px; }
  .card--back .brand { left: 62px; top: 48px; }
  .card--back .brand__mark { width: 88px; height: 88px; border: 4px solid var(--slate); }
  .card--back .brand__name { color: var(--slate); font-size: 33px; }

  .contact { position: absolute; left: 34px; top: 200px; color: var(--ink); }
  .contact__name { color: var(--teal); font-weight: 700; font-size: 20px; }
  .contact__role { font-size: 12px; margin: 3px 0 12px; }
  .contact__line { font-size: 12px; line-height: 1.5; }
  .contact__label { color: var(--teal); }

  .address { position: absolute; left: 372px; top: 262px; color: var(--white); font-size: 12px; line-height: 1.5; }
  .address .contact__label { color: var(--teal); }
</style>
</head>
<body>

<section class="card card--front" aria-label="Vorderseite">
  <div class="brand">
    <span class="brand__mark" aria-hidden="true"></span>
    <p class="brand__name">Vestaluk<br>Chirurgie</p>
  </div>
</section>

<section class="card card--back" aria-label="Rückseite">
  <svg class="card__wave" viewBox="0 0 540 338" aria-hidden="true">
    <path d="M0,176 C150,136 330,136 420,106 C480,86 520,56 540,26" fill="none" stroke="var(--slate)" stroke-width="2"/>
    <path d="M0,184 C150,144 330,144 420,114 C480,94 520,64 540,34" fill="none" stroke="var(--teal)" stroke-width="5"/>
    <path d="M0,196 C150,156 330,156 420,126 C480,106 520,76 540,46 L540,338 L0,338 Z" fill="var(--slate)"/>
  </svg>

  <div class="brand">
    <span class="brand__mark" aria-hidden="true"></span>
    <p class="brand__name">Vestaluk<br>Chirurgie</p>
  </div>

  <div class="contact">
    <p class="contact__name">Priv. Doz. DDr. Corinna Vestaluk</p>
    <p class="contact__role">Fachärztin für Allgemein- &amp; Viszeralchirurgie</p>
    <p class="contact__line"><span class="contact__label">Tel:</span>123 456 789</p>
    <p class="contact__line"><span class="contact__label">Mobil:</span>123 456 7890</p>
    <p class="contact__line"><span class="contact__label">Webseite:</span>www.vestalukchirurgie</p>
    <p class="contact__line"><span class="contact__label">Email:</span>info@vestalukchirurgie</p>
  </div>

  <div class="address">
    <p><span class="contact__label">Address:</span>123 Your address</p>
    <p>Lindenfeld, Lindenfeld</p>
  </div>
</section>

</body>
</html>
```